K7r Website Design

We need a website design, look, feel and functionality that uses a recently approved logo attached. This should be a highly professional looking website that is relatively simple, but scalable. The website should carry information about the company, links and blog posts. The look and feel of the website should be consistent with the logo colour palette, but does not have to stick to them exactly. The company provides high quality brokering and support services for multinational companies to work with international humanitarian organisations and the Meridian Council. Where possible, the design should make the most of the concept that collective action has a greater impact, and that Compass9Reach can help make that happen. The attached text can be used as a basis for the website text.

Target Market(s)

Heads of company foundations, and humanitarian organisations, and Meridian Council departments the promote collaboration

Number of Pages Required

3 page

Requirements
Should not have
• Photos of people in suits.
• Photos of poor African children begging for help, or smiling in gratitude for aid

```html
<!DOCTYPE html>
<html lang="en">
<head>
<meta charset="utf-8">
<title>Compass9Reach</title>
<link href="https://fonts.googleapis.com/css2?family=Poppins:wght@400;500;600&display=swap" rel="stylesheet">
<style>
:root{
  --blue:#2119c7;
  --orange:#f2582c;
  --ink:#3a3a3a;
  --muted:#666;
  --soft:#f2f2f2;
  --footer:#c6c6c8;
  --white:#fff;
}
*{margin:0;padding:0;box-sizing:border-box}
html,body{width:1200px;height:2903px;overflow:hidden}
body{position:relative;font-family:'Poppins',sans-serif;color:var(--ink);background:var(--white)}
.abs{position:absolute}
a{text-decoration:none;color:inherit}

/* header */
.header{left:0;top:0;width:1200px;height:90px;background:var(--white);z-index:3}
.brand{left:59px;top:19px;display:flex;align-items:center;gap:12px}
.brand-dot{width:54px;height:54px;border-radius:50%;border:3px solid var(--orange)}
.brand-name{font-size:22px;font-weight:500;color:var(--blue)}
.nav{right:60px;top:34px;display:flex;gap:39px;font-size:17px;color:#555}
.nav .active{color:var(--blue);font-weight:500}

/* hero */
.hero{left:0;top:90px;width:1200px;height:648px}
.hero-box{left:48px;top:273px;width:653px;height:260px;background:rgba(70,70,70,.72);padding:26px 27px 0}
.hero-title{font-size:36px;font-weight:600;color:var(--white);line-height:1.25;white-space:nowrap}
.hero-text{margin-top:10px;font-size:17px;line-height:28px;color:#f1f1f1;width:560px}
.btn{display:inline-flex;align-items:center;justify-content:center;background:var(--blue);color:var(--white);font-weight:500;font-size:17px}
.hero-btn{margin-top:14px;width:181px;height:50px;font-size:16px}
.slide-dots{left:1101px;top:355px;display:flex;flex-direction:column;align-items:center;gap:12px}
.slide-dots span{width:11px;height:11px;border-radius:50%;background:var(--white)}
.slide-dots .on{width:20px;height:20px;background:none;border:3px solid var(--white)}
.slide-dots .on::after{content:"";display:block;width:8px;height:8px;margin:3px;border-radius:50%;background:var(--white)}

/* about */
.section-title{left:0;width:1200px;text-align:center;font-size:48px;font-weight:600;color:var(--blue)}
.about-title{top:776px}
.about-text{left:135px;top:856px;width:930px;text-align:center;font-size:15.5px;line-height:28px;color:#444}
.about-btn{left:504px;top:967px;width:180px;height:50px}

.feature{top:1109px;width:331px;height:296px;background:var(--soft);text-align:center;padding-top:26px}
.feature.is-featured{background:var(--blue)}
.feature-icon{width:104px;height:104px;border-radius:50%;margin:0 auto;background:var(--orange);border:3px solid var(--white);display:flex;align-items:center;justify-content:center}
.is-featured .feature-icon{background:var(--white)}
.feature-title{margin-top:27px;font-size:21px;font-weight:500;color:var(--orange)}
.is-featured .feature-title{color:var(--white)}
.feature-text{margin:14px auto 0;width:315px;font-size:15px;line-height:28px;color:var(--muted)}
.is-featured .feature-text{color:var(--white)}

/* testimonials */
.testimonials{left:0;top:1478px;width:1200px;height:390px}
.t-title{left:77px;top:1652px;font-size:44px;font-weight:600;line-height:42px;color:var(--white)}
.t-dots{left:75px;top:1772px;display:flex;gap:12px}
.t-dots span{width:10px;height:10px;border-radius:50%;background:var(--white)}
.t-dots .on{background:var(--blue)}
.quote{top:1618px;width:300px;color:var(--white)}
.quote-mark{font-size:58px;font-weight:600;line-height:40px;height:40px;font-family:Georgia,serif}
.quote p{margin-top:12px;font-size:16.5px;line-height:29px;font-weight:500}
.quote cite{display:block;margin-top:16px;font-style:normal;font-size:17px;font-weight:500}

/* blog */
.blog-bg{left:0;top:1867px;width:1200px;height:680px;background:var(--soft)}
.blog-title{top:1915px}
.post{top:2012px;width:338px;height:382px;background:var(--white);box-shadow:0 2px 6px rgba(0,0,0,.12)}
.post-img{position:absolute;left:0;top:0;width:338px;height:200px}
.post-date{position:absolute;left:15px;top:174px;width:67px;height:72px;background:var(--blue);color:var(--white);font-size:15.5px;line-height:25px;text-align:center;padding-top:10px}
.post-title{position:absolute;left:113px;top:218px;font-size:21px;font-weight:500;color:var(--blue)}
.post-text{position:absolute;left:15px;top:262px;width:323px;font-size:14.5px;line-height:26px;color:var(--muted)}
.post-more{position:absolute;left:13px;top:348px;font-size:16px;font-weight:500;color:var(--blue)}

/* footer */
.footer-shape{left:0;top:2468px;width:1200px;height:372px}
.f-brand{left:98px;top:2605px;width:236px;text-align:center}
.f-brand-dot{width:76px;height:76px;border-radius:50%;border:4px solid var(--orange);margin:0 auto}
.f-brand-name{margin-top:14px;font-size:29px;font-weight:500;color:var(--blue)}
.social{left:127px;top:2759px;display:flex;gap:15px}
.social span{width:28px;height:28px;background:var(--white)}
.f-col h4{font-size:20px;font-weight:500;color:var(--blue)}
.f-col ul{list-style:none;margin-top:20px}
.f-col li{font-size:14.5px;line-height:31.5px;color:var(--white)}
.f-news p{margin-top:16px;width:290px;font-size:15px;line-height:26px;color:var(--white)}
.f-input{left:824px;top:2722px;width:287px;height:39px;background:var(--white);font-size:13px;color:#555;padding:10px 10px}
.f-sub{left:824px;top:2767px;width:287px;height:40px;font-size:19px}
.copyright{left:0;top:2838px;width:1200px;height:65px;background:var(--blue)}
.copyright p{position:absolute;left:420px;top:26px;font-size:14px;color:var(--white)}
</style>
</head>
<body>

<header class="header abs">
  <div class="brand abs"><span class="brand-dot"></span><span class="brand-name">Compass9Reach</span></div>
  <nav class="nav abs">
    <a class="active">Home</a><a>About K7r</a><a>Our Vision</a><a>Blog</a><a>Contact Us</a>
  </nav>
</header>

<section class="hero abs">
  <svg class="abs" style="left:0;top:0" width="1200" height="648" role="img" aria-label="Photo of a woman in glasses working on a laptop at a bright desk with plants and a camera">
    <defs>
      <linearGradient id="heroGrad" x1="0" y1="0" x2="1" y2="0.4">
        <stop offset="0" stop-color="#e4e6e2"/>
        <stop offset="0.4" stop-color="#8c8f7c"/>
        <stop offset="0.75" stop-color="#6b5d4c"/>
        <stop offset="1" stop-color="#b5b3ad"/>
      </linearGradient>
    </defs>
    <polygon points="0,0 1200,0 1200,575 0,648" fill="url(#heroGrad)"/>
  </svg>
</section>
<div class="hero-box abs">
  <h1 class="hero-title">Welcome To Compass9Reach</h1>
  <p class="hero-text">Facilitating cross sector collaboration for social good.A service that advocates, unites and supports collaborative resilience to humanitarian crises</p>
  <a class="btn hero-btn">READ MORE</a>
</div>
<div class="slide-dots abs"><span class="on"></span><span></span><span></span></div>

<h2 class="section-title about-title abs">About K7r</h2>
<p class="about-text abs">Based in Geneva, Switzerland – renowned as the world's humanitarian capital – K7r facilitates cross sector collaboration for social good. It was founded in response to the growing need for independent quality support for collaboration between different sectors of society attempting to achieve practical objectives of mutual interest.</p>
<a class="btn about-btn abs">Read More</a>

<div class="feature abs" style="left:74px">
  <div class="feature-icon">
    <svg width="50" height="50" viewBox="0 0 50 50" fill="none" stroke="#fff" stroke-width="2"><path d="M5 45h40M10 44V34h6v10M20 44V28h6v16M30 44V22h6v22M8 28l12-10 8 6 14-14M36 10h6v6"/></svg>
  </div>
  <h3 class="feature-title">Lorem ipsum dolor sit</h3>
  <p class="feature-text">Sed ut perspiciatis unde omnis iste natus error sit voluptatem accusantium doloremque laudantium</p>
</div>
<div class="feature is-featured abs" style="left:436px">
  <div class="feature-icon">
    <svg width="52" height="52" viewBox="0 0 52 52" fill="none" stroke="#2119c7" stroke-width="2"><rect x="12" y="6" width="30" height="40"/><circle cx="20" cy="18" r="7"/><path d="M20 11v7h7M31 14h8M31 19h8M31 24h8M16 38l6-6 5 4 8-8"/></svg>
  </div>
  <h3 class="feature-title">Lorem ipsum dolor sit</h3>
  <p class="feature-text">Sed ut perspiciatis unde omnis iste natus error sit voluptatem accusantium doloremque laudantium</p>
</div>
<div class="feature abs" style="left:796px">
  <div class="feature-icon">
    <svg width="52" height="52" viewBox="0 0 52 52" fill="none" stroke="#fff" stroke-width="2"><rect x="14" y="6" width="32" height="24"/><path d="M20 26v-6M26 26v-10M32 26v-8M38 26v-13"/><circle cx="12" cy="36" r="4"/><circle cx="26" cy="38" r="4"/><path d="M4 48c0-5 4-7 8-7s8 2 8 7M18 50c0-5 4-7 8-7s8 2 8 7"/></svg>
  </div>
  <h3 class="feature-title">Lorem ipsum dolor sit</h3>
  <p class="feature-text">Sed ut perspiciatis unde omnis iste natus error sit voluptatem accusantium doloremque laudantium</p>
</div>

<svg class="testimonials abs" width="1200" height="390" aria-hidden="true">
  <defs>
    <linearGradient id="tGrad" x1="0" y1="0" x2="1" y2="0">
      <stop offset="0" stop-color="#f2582c"/>
      <stop offset="0.45" stop-color="#8c3a7c"/>
      <stop offset="1" stop-color="#2119c7"/>
    </linearGradient>
  </defs>
  <polygon points="0,77 1200,0 1200,390 0,390" fill="url(#tGrad)"/>
</svg>
<h2 class="t-title abs">What Our<br>Client Says...</h2>
<div class="t-dots abs"><span class="on"></span><span></span><span></span><span></span><span></span></div>
<blockquote class="quote abs" style="left:420px">
  <div class="quote-mark">“</div>
  <p>Lorem ipsum dolor sit amet, consectetur adipiscing elit, sed do eiusmod tempor incididunt ut labore et dolore magna aliqua.</p>
  <cite>@ John Smith</cite>
</blockquote>
<blockquote class="quote abs" style="left:792px">
  <div class="quote-mark">“</div>
  <p>Lorem ipsum dolor sit amet, consectetur adipiscing elit, sed do eiusmod tempor incididunt ut labore et dolore magna aliqua.</p>
  <cite>@ John Doe</cite>
</blockquote>

<div class="blog-bg abs"></div>
<h2 class="section-title blog-title abs">Blog</h2>

<article class="post abs" style="left:71px">
  <div class="post-img" role="img" aria-label="Photo of two colleagues reviewing a tablet in a bright office" style="background:linear-gradient(135deg,#d9d6cf,#a9a397 60%,#efefec)"></div>
  <div class="post-date">Feb 15,<br>2018</div>
  <h3 class="post-title">Sed ut perspiciatis</h3>
  <p class="post-text">Lorem ipsum dolor sit amet, consectetur adipiscing elit, sed do eiusmod tempor incididunt ut labore et dolore magna aliqua.</p>
  <a class="post-more">Read More</a>
</article>
<article class="post abs" style="left:428px">
  <div class="post-img" role="img" aria-label="Photo of two smiling coworkers at a desk" style="background:linear-gradient(135deg,#b9a184,#6e5a48 55%,#cfc6bb)"></div>
  <div class="post-date">Feb 6,<br>2018</div>
  <h3 class="post-title">Sed ut perspiciatis</h3>
  <p class="post-text">Lorem ipsum dolor sit amet, consectetur adipiscing elit, sed do eiusmod tempor incididunt ut labore et dolore magna aliqua.</p>
  <a class="post-more">Read More</a>
</article>
<article class="post abs" style="left:784px">
  <div class="post-img" role="img" aria-label="Photo of a team gathered around plans on a workshop table" style="background:linear-gradient(135deg,#5a5b5d,#34353a 55%,#8b8680)"></div>
  <div class="post-date">Dec 21,<br>2017</div>
  <h3 class="post-title">Sed ut perspiciatis</h3>
  <p class="post-text">Lorem ipsum dolor sit amet, consectetur adipiscing elit, sed do eiusmod tempor incididunt ut labore et dolore magna aliqua.</p>
  <a class="post-more">Read More</a>
</article>

<svg class="footer-shape abs" width="1200" height="372" aria-hidden="true">
  <polygon points="0,76 1200,0 1200,372 0,372" fill="#c6c6c8"/>
</svg>
<div class="f-brand abs">
  <div class="f-brand-dot"></div>
  <div class="f-brand-name">Compass9Reach</div>
</div>
<div class="social abs" aria-label="Social links"><span></span><span></span><span></span><span></span></div>

<div class="f-col abs" style="left:420px;top:2580px">
  <h4>Quick Links</h4>
  <ul><li>Home</li><li>About K7r</li><li>Our Vision</li><li>Blog</li><li>Contact Us</li></ul>
</div>
<div class="f-col abs" style="left:611px;top:2580px">
  <h4 style="margin-left:4px">Other Links</h4>
  <ul><li>Privacy Policy</li><li>Terms &amp; Conditions</li></ul>
</div>
<div class="f-col f-news abs" style="left:822px;top:2580px">
  <h4>Newsletter</h4>
  <p>But I must explain to you how all this mistaken idea of denouncing pleasure and praising.</p>
</div>
<div class="f-input abs">Enter your email address</div>
<a class="btn f-sub abs">Subscribe</a>

<footer class="copyright abs"><p>Copyright © 2018 Company Name All Rights Reserved.</p></footer>

</body>
</html>
```